Car finance company business card

Create a nice business card for our car financing company , Visit our website www.birchlanefinance.com for the phone number and idea of the company look. Please do not be afraid to be creative. Name on card Is Marc-Antoine Beaulieu and phone number is on our website adress of business is
27816 Boulevard Saint-Orvel,
Val-Orvel, QC K4R 2T8

```html
<!DOCTYPE html>
<html lang="en">
<head>
<meta charset="utf-8">
<title>Birch Lane Finance – Business Card</title>
<link rel="stylesheet" href="https://fonts.googleapis.com/css2?family=Montserrat:wght@800&family=Roboto:wght@400;700&display=swap">
<style>
  :root {
    --bg: #262626;
    --card-dark: #3a3a3b;
    --card-light: #ffffff;
    --orange: #ee6a25;
    --violet: #5553a8;
    --sky: #7e9bd6;
    --ink: #222222;
    --steel: #c9c9cc;
  }
  html, body {
    margin: 0;
    width: 1200px;
    height: 895px;
    overflow: hidden;
    background: var(--bg);
  }
  .canvas {
    position: relative;
    width: 1200px;
    height: 895px;
  }
  .card {
    position: absolute;
    width: 620px;
    height: 354px;
    border-radius: 4px;
    overflow: hidden;
    box-shadow: 0 10px 30px rgba(0,0,0,.45);
  }
  .card--front {
    left: 80px;
    top: 80px;
    background: var(--card-dark);
    display: flex;
    align-items: center;
    justify-content: center;
  }
  .card--back {
    left: 500px;
    top: 460px;
    background: var(--card-light);
  }
  .brand {
    display: flex;
    align-items: center;
    gap: 14px;
    font-family: "Roboto", sans-serif;
    font-weight: 700;
    text-transform: uppercase;
    line-height: 1;
  }
  .brand__dot {
    width: 26px;
    height: 26px;
    border-radius: 50%;
    flex: none;
  }
  .card--front .brand { color: var(--steel); font-size: 40px; }
  .card--front .brand__dot { background: var(--steel); width: 34px; height: 34px; }
  .card--back .brand {
    position: absolute;
    left: 372px;
    top: 92px;
    color: var(--ink);
    font-size: 22px;
    width: 220px;
  }
  .card--back .brand__dot { background: var(--orange); }
  .contact {
    position: absolute;
    right: 318px;
    top: 62px;
    text-align: right;
    font-family: "Roboto", sans-serif;
    color: var(--ink);
  }
  .contact__name {
    font-family: "Montserrat", sans-serif;
    font-weight: 800;
    font-size: 19px;
    color: var(--orange);
    text-transform: uppercase;
    margin: 0;
    letter-spacing: .2px;
  }
  .contact__role { font-size: 15px; margin: 2px 0 18px; }
  .contact__line { font-size: 15px; margin: 0; line-height: 1.35; }
  .contact__gap { height: 14px; }
  .contact__item { display: flex; align-items: center; justify-content: flex-end; gap: 10px; }
  .contact__item svg { width: 13px; height: 13px; flex: none; }
  .divider {
    position: absolute;
    left: 330px;
    width: 2px;
  }
  .divider--top { top: 48px; height: 34px; background: var(--violet); }
  .divider--mid { top: 114px; height: 34px; background: var(--orange); }
  .divider--low { top: 180px; height: 52px; background: var(--violet); }
  .waves {
    position: absolute;
    left: 0;
    bottom: 0;
    width: 620px;
    height: 170px;
  }
</style>
</head>
<body>
<main class="canvas">
  <section class="card card--front" aria-label="Card front">
    <div class="brand">
      <span class="brand__dot"></span>
      <span class="brand__name">Birch Lane Finance</span>
    </div>
  </section>

  <section class="card card--back" aria-label="Card back">
    <div class="contact">
      <p class="contact__name">Marc-Antoine Beaulieu</p>
      <p class="contact__role">Director</p>
      <p class="contact__line">27816 Boulevard Saint-Orvel,</p>
      <p class="contact__line">Val-Orvel, QC K4R 2T8</p>
      <div class="contact__gap"></div>
      <p class="contact__line contact__item">(450) 555-0187
        <svg viewBox="0 0 16 16" aria-hidden="true"><path fill="var(--violet)" d="M3 1l3 3-2 2c1 2 3 4 5 5l2-2 3 3-2 3C7 15 1 9 1 3z"/></svg>
      </p>
      <p class="contact__line contact__item">info@birchlanefinance.com
        <svg viewBox="0 0 16 16" aria-hidden="true"><rect x="1" y="3" width="14" height="10" fill="var(--orange)"/><path d="M1 3l7 6 7-6" fill="none" stroke="#fff" stroke-width="1.4"/></svg>
      </p>
      <p class="contact__line contact__item">www.birchlanefinance.com
        <svg viewBox="0 0 16 16" aria-hidden="true"><circle cx="8" cy="8" r="7" fill="var(--sky)"/><path d="M1 8h14M8 1c-3 4-3 10 0 14M8 1c3 4 3 10 0 14" fill="none" stroke="#fff" stroke-width="1"/></svg>
      </p>
    </div>
    <span class="divider divider--top"></span>
    <span class="divider divider--mid"></span>
    <span class="divider divider--low"></span>

    <div class="brand">
      <span class="brand__dot"></span>
      <span class="brand__name">Birch Lane<br>Finance</span>
    </div>

    <svg class="waves" viewBox="0 0 620 170" preserveAspectRatio="none" aria-hidden="true">
      <path d="M0 120 C100 98 200 86 310 80 C200 94 100 114 0 142 Z" fill="var(--orange)"/>
      <path d="M300 102 C420 78 520 50 620 10 L620 20 C520 60 420 88 300 106 Z" fill="var(--sky)"/>
      <path d="M0 150 C200 132 400 95 620 28 L620 170 L0 170 Z" fill="var(--violet)"/>
    </svg>
  </section>
</main>
</body>
</html>
```